Buch-/E-Book-Cover für einen Thriller
Zielgruppe
Unter dem Pseudonym Merle Voss (Website: www.merle-voss-beispiel.de) veröffentliche ich Thriller zum Zeitgeschehen. (Beispiel: Trandor - ein kalter Handel)
Aufgabenstellung
Für das Ebook und das Taschenbuch des neuen Thrillers „Der Riegel“ benötige ich ein aussagefähiges, eigenständiges und ins Auge fallendes Cover. Die Grafik kann sich in Farbe und Form bewusst von „Trandor“ abheben, der Fokus liegt auf dem Thema des Thrillers. In anhängender .pdf-Datei sind Handlung und Figuren detailliert beschrieben; keine Bange vor der Seitenzahl - jede Figur hat eine eigene Seite :-) , daher die Größe.

```html
<!DOCTYPE html>
<html lang="de">
<head>
<meta charset="utf-8">
<title>Der Riegel – Umschlag</title>
<link rel="stylesheet" href="https://fonts.googleapis.com/css2?family=Josefin+Sans:wght@100;300&family=Quicksand:wght@400;500;600&display=swap">
<style>
  :root {
    --paper: #dadada;
    --paper-light: #e4e4e4;
    --ink: #1e1e1e;
    --ink-soft: #2c2c2c;
    --title-light: #f4f4f4;
    --title-grey: #d8d8d8;
    --accent-red: #6e0f0f;
    --shadow-dark: #0c0c0c;
    --white: #ffffff;
  }
  * { margin: 0; padding: 0; box-sizing: border-box; }
  html, body { width: 1200px; height: 813px; overflow: hidden; }
  body { font-family: "Quicksand", sans-serif; color: var(--ink); }

  .cover-wrap {
    position: relative;
    width: 1200px;
    height: 813px;
    background: radial-gradient(ellipse at 50% 45%, var(--paper-light) 0%, var(--paper) 70%, #d2d2d2 100%);
    overflow: hidden;
  }

  /* Back cover */
  .back-mini-title {
    position: absolute;
    left: 185px; width: 200px;
    text-align: center;
    font-family: "Quicksand", sans-serif;
  }
  .back-mini-title.top { top: 86px; font-size: 16px; font-weight: 400; letter-spacing: -1px; }
  .back-mini-title.bottom { top: 190px; font-size: 21px; font-weight: 600; letter-spacing: 0.5px; color: var(--ink-soft); }
  .back-emblem {
    position: absolute;
    left: 227px; top: 108px; width: 116px; height: 78px;
    border-radius: 50%;
    background: radial-gradient(ellipse at 60% 55%, var(--shadow-dark) 0%, #333 55%, rgba(60,60,60,0) 75%);
  }
  .blurb {
    position: absolute;
    left: 113px; top: 278px; width: 345px;
    font-size: 14.6px; line-height: 19.7px;
    text-align: justify; font-weight: 500;
    color: var(--ink);
  }
  .code-field {
    position: absolute;
    left: 298px; top: 650px; width: 161px; height: 106px;
    background: var(--white);
  }

  /* Spine */
  .spine-emblem {
    position: absolute;
    left: 577px; top: 78px; width: 46px; height: 67px;
    border-radius: 50%;
    background: radial-gradient(ellipse at 55% 40%, var(--shadow-dark) 0%, #333 55%, rgba(60,60,60,0) 75%);
  }
  .spine-title {
    position: absolute;
    left: 601px; top: 402px;
    transform: translate(-50%, -50%) rotate(-90deg);
    white-space: nowrap;
    font-size: 36px; font-weight: 500; letter-spacing: 2px;
    color: var(--ink-soft);
  }
  .spine-author {
    position: absolute;
    left: 601px; top: 685px;
    transform: translate(-50%, -50%) rotate(-90deg);
    white-space: nowrap;
    font-size: 16px; font-weight: 500; letter-spacing: 0.5px;
    color: var(--ink-soft);
  }

  /* Front cover */
  .front-author {
    position: absolute;
    left: 760px; width: 302px; top: 84px;
    text-align: center;
    font-family: "Josefin Sans", sans-serif;
    font-weight: 300; font-size: 29px;
    color: var(--ink);
  }
  .front-artwork {
    position: absolute;
    left: 717px; top: 176px; width: 394px; height: 496px;
    background:
      radial-gradient(ellipse at 62% 45%, var(--shadow-dark) 0%, #1a1a1a 35%, rgba(40,40,40,0.55) 60%, rgba(90,90,90,0) 78%),
      linear-gradient(180deg, rgba(80,80,80,0) 0%, rgba(70,70,70,0.25) 20%, rgba(30,30,30,0.5) 80%, rgba(100,100,100,0) 100%);
    border-radius: 46% 46% 40% 40%;
  }
  .front-title-top {
    position: absolute;
    left: 790px; top: 222px;
    font-family: "Josefin Sans", sans-serif;
    font-weight: 100; font-size: 200px; line-height: 1;
    letter-spacing: -10px;
    color: var(--title-light);
  }
  .front-title-bottom {
    position: absolute;
    left: 797px; top: 482px; width: 232px;
    font-family: "Quicksand", sans-serif;
    font-weight: 600; font-size: 54px; line-height: 1;
    letter-spacing: 1px;
    color: var(--title-grey);
  }
  .genre {
    position: absolute;
    left: 760px; width: 302px; top: 705px;
    text-align: center;
    font-family: "Josefin Sans", sans-serif;
    font-weight: 300; font-size: 29px;
    color: var(--accent-red);
  }
</style>
</head>
<body>
  <main class="cover-wrap">
    <section class="back-cover">
      <div class="back-mini-title top">DER</div>
      <div class="back-emblem" role="img" aria-label="Dunkle Silhouette eines Ungeborenen"></div>
      <div class="back-mini-title bottom">RIEGEL</div>
      <p class="blurb">Lorem ipsum dolor sit amet, consetetur sadipscing elitr, sed diam nonumy eirmod tempor invidunt ut labore et dolore magna aliquyam erat, sed diam voluptua. At vero eos et accusam et justo duo dolores et ea rebum. Stet clita kasd gubergren, no sea takimata sanctus est Lorem ipsum dolor sit amet. Lorem ipsum dolor sit amet, consetetur sadipscing elitr, sed diam nonumy eirmod tempor invidunt ut labore et dolore magna aliquyam erat, sed diam voluptua. At vero eos et accusam et justo duo dolores et ea rebum. Stet clita kasd gubergren, no sea takimata sanctus est Lorem ipsum dolor sit amet.</p>
      <div class="code-field"></div>
    </section>

    <section class="spine">
      <div class="spine-emblem" role="img" aria-label="Kleine Silhouette eines Ungeborenen"></div>
      <div class="spine-title">DER RIEGEL</div>
      <div class="spine-author">Merle Voss</div>
    </section>

    <section class="front-cover">
      <div class="front-author">merle voss</div>
      <div class="front-artwork" role="img" aria-label="Doppelbelichtung: Silhouette eines Ungeborenen mit kahlen Bäumen oben und dunklem Nadelwald unten"></div>
      <div class="front-title-top">DER</div>
      <div class="front-title-bottom">RIEGEL</div>
      <div class="genre">thriller</div>
    </section>
  </main>
</body>
</html>
```